Clean professional business card design

Need a professional looking, high quality card and letterhead design. Business card would prefer to have a grey tone to the background.

Back of card needs to have: "Securities offered through Volmara Wealth Partners LLC (doing Insurance business in CA as VWPGS Insurance Agency), member OBREK/TADL. Advisory services offered through Volmara Asset Counsel LLC. Volmara entities are under separate ownership from any other named entity. [employee name] CA Insurance Lic #7K24903

Industry/Entity Type

Financial Planning

Font styles to use
Serif
Sans Serif

Requirements
Must have
• Customization of text so that I can adjust for other employee

```html
<!DOCTYPE html>
<html lang="en">
<head>
<meta charset="utf-8">
<title>Keystone Wealth Advisers – Business Card</title>
<link rel="stylesheet" href="https://fonts.googleapis.com/css2?family=Work+Sans:wght@400;500&display=swap">
<style>
  :root {
    --brand-blue: #0b6fbb;
    --back-blue: #0e6cb3;
    --ink: #4a4a4a;
    --card-grey: #eceef0;
    --band-grey: #9a9a9a;
    --stage: #f8f9fa;
    --white: #ffffff;
  }
  html, body {
    margin: 0;
    width: 1200px;
    height: 1000px;
    overflow: hidden;
    background: var(--stage);
    font-family: "Work Sans", Arial, sans-serif;
  }
  .canvas { position: relative; width: 1200px; height: 1000px; }
  .card {
    position: absolute;
    left: 240px;
    width: 696px;
    height: 395px;
    border-radius: 22px;
    overflow: hidden;
    box-shadow: 0 6px 14px rgba(0,0,0,.18);
  }
  .card--front { top: 83px; background: var(--card-grey); }
  .card--back {
    top: 520px; height: 397px;
    background: linear-gradient(180deg, #1172bb 0%, var(--back-blue) 100%);
  }

  .card__bands { position: absolute; left: 0; bottom: 0; width: 696px; height: 40px; }

  .wordmark {
    position: absolute;
    left: 0;
    width: 396px;
    text-align: center;
    font-weight: 500;
    text-transform: uppercase;
  }
  .card--front .wordmark { top: 205px; color: var(--brand-blue); }
  .wordmark__line1 { display: block; font-size: 33px; letter-spacing: 1px; line-height: 38px; }
  .wordmark__line2 { display: block; font-size: 19px; letter-spacing: 2.5px; line-height: 28px; }

  .divider {
    position: absolute;
    left: 358px; top: 105px;
    width: 2px; height: 187px;
    background: var(--brand-blue);
  }
  .contact { position: absolute; left: 397px; top: 100px; color: var(--ink); }
  .contact__name {
    margin: 0;
    font-size: 25px; font-weight: 500; letter-spacing: 1.5px;
    color: var(--brand-blue);
  }
  .contact__role { margin: 6px 0 0; font-size: 15px; letter-spacing: .5px; color: #333; }
  .contact__address { margin: 20px 0 0; font-size: 15px; line-height: 20px; }
  .contact__list { list-style: none; padding: 0; margin: 21px 0 0; font-size: 15px; line-height: 20px; }
  .contact__list li { display: flex; align-items: center; gap: 9px; }
  .contact__list svg { width: 10px; height: 10px; fill: var(--brand-blue); }

  .card--back .wordmark {
    width: 696px; top: 192px; color: var(--white);
  }
  .card--back .wordmark__line1 { font-size: 36px; line-height: 42px; }
  .card--back .wordmark__line2 { font-size: 21px; line-height: 30px; }
  .back__disclosure {
    position: absolute; left: 60px; width: 576px; top: 278px;
    margin: 0;
    text-align: center; color: var(--white);
    font-size: 10.5px; line-height: 14px; opacity: .92;
  }
  .back__web {
    position: absolute; left: 0; width: 696px; top: 350px; margin: 0;
    text-align: center; color: var(--white);
    font-size: 16px; letter-spacing: 1.5px;
  }
</style>
</head>
<body>
<main class="canvas">
  <section class="card card--front" aria-label="Business card front">
    <div class="wordmark">
      <span class="wordmark__line1">Keystone</span>
      <span class="wordmark__line2">Wealth Advisers</span>
    </div>
    <div class="divider"></div>
    <div class="contact">
      <h1 class="contact__name">DANIEL HART</h1>
      <p class="contact__role">Founder</p>
      <p class="contact__address">482 Harbor View Rd.<br>Lakeside Point, FL 33901</p>
      <ul class="contact__list">
        <li><svg viewBox="0 0 10 10" aria-hidden="true"><path d="M2 0h2l1 2.5-1.3 1a6 6 0 0 0 2.8 2.8l1-1.3L10 6v2a2 2 0 0 1-2 2A8 8 0 0 1 0 2a2 2 0 0 1 2-2z"/></svg>555-318-4026</li>
        <li><svg viewBox="0 0 10 10" aria-hidden="true"><path d="M0 2h10v6H0z M0.8 2.6v.6L5 6l4.2-2.8v-.6L5 5.4z" fill-rule="evenodd"/></svg>dhart@keystonewealth.com</li>
        <li><svg viewBox="0 0 10 10" aria-hidden="true"><circle cx="5" cy="5" r="4.5" fill="none" stroke="#0b6fbb" stroke-width="1"/><path d="M0.5 5h9M5 .5c-2.5 2.8-2.5 6.2 0 9M5 .5c2.5 2.8 2.5 6.2 0 9" fill="none" stroke="#0b6fbb" stroke-width=".8"/></svg>www.KeystoneWealth.com</li>
      </ul>
    </div>
    <svg class="card__bands" viewBox="0 0 696 40" aria-hidden="true">
      <rect x="0" y="25" width="360" height="15" fill="var(--band-grey)"/>
      <polygon points="349,40 384,9 696,9 696,40" fill="var(--brand-blue)"/>
    </svg>
  </section>

  <section class="card card--back" aria-label="Business card back">
    <div class="wordmark">
      <span class="wordmark__line1">Keystone</span>
      <span class="wordmark__line2">Wealth Advisers</span>
    </div>
    <p class="back__disclosure">Securities offered through Volmara Wealth Partners LLC (doing Insurance business in CA as VWPGS Insurance Agency), member OBREK/TADL. Advisory services offered through Volmara Asset Counsel LLC. Volmara entities are under separate ownership from any other named entity. <span class="back__employee">Daniel Hart</span> CA Insurance Lic #7K24903</p>
    <p class="back__web">www.keystonewealth.com</p>
  </section>
</main>
</body>
</html>
```